New Business and Accounting Software need a Web Site

The website is for a Business and Accounting Software that has 8 products.
Each product has its owns logo and color, when you do the design have in consideration that we are looking the experience that when you change from one product page to another the look and feel adjust to the color and logo of the product.
The product are:
Ventas (Sales)
Compras (Purchases)
Contabilidad (Accounting)
Presupuesto (Budget)
Inventarios (Inventory)
Bancos (Banks)
NĂ³mina RH (Human Resources Payroll)
CRM (Customer Relationship Manager)

You can see how the main logo and variations are used in each page
- https://www.ufta.com/
- https://www.vemi.com/
- https://www.prulvin.com/

Our goal is to be similar to them.

I have created a word document to explain what I want.
You need to design:
1 Home Page
1 Product Landing Page
1 Product Detail Page
1 Price Page

I am attaching:
1. Main Logo
2. 8 Product Logos
3. Website Idea, you can create your own idea.

You are welcome to use other icons for the each product if you want.

Target Market(s)

Independet professionals and Small and Medium Companies

Industry/Entity Type

Business and Accounting Software

Coding

Coded - Design and coding required

Colors
0054AA
0677BA
7BADD7
CADEEF
E8F1F8

Requirements
Must have
• Must show all products in the main page

```html
<!DOCTYPE html>
<html lang="es">
<head>
<meta charset="utf-8">
<title>tavo.cr — Sistema Contable y Facturación en la nube</title>
<link href="https://fonts.googleapis.com/css2?family=Poppins:wght@400;500;600;700&display=swap" rel="stylesheet">
<style>
:root{
  --blue:#0054AA;
  --blue-mid:#0677BA;
  --blue-soft:#7BADD7;
  --blue-pale:#CADEEF;
  --blue-mist:#E8F1F8;
  --green:#5BC21F;
  --grey-bg:#F2F2F2;
  --text:#666;
  --white:#fff;
}
*{margin:0;padding:0;box-sizing:border-box}
html,body{width:1200px;height:4038px;overflow:hidden}
body{font-family:'Poppins',sans-serif;color:var(--text);background:var(--white);position:relative}
.abs{position:absolute}
.brand{display:flex;align-items:center;gap:8px;font-weight:700;color:var(--blue);font-size:38px}
.brand .dot{width:50px;height:50px;border-radius:50%;background:var(--blue)}
/* header */
.site-header{position:absolute;top:0;left:0;width:1200px;height:75px;background:var(--white)}
.site-header .brand{position:absolute;left:58px;top:9px}
.nav{position:absolute;left:548px;top:27px;display:flex;gap:40px;font-size:14px;color:#555}
.nav .active{color:var(--blue)}
.btn{display:inline-block;border-radius:20px;background:var(--blue);color:var(--white);font-size:13px;text-align:center}
.btn-sign{left:927px;top:22px;width:88px;height:36px;line-height:36px}
.btn-trial{left:1037px;top:22px;width:103px;height:36px;line-height:36px}
/* hero */
.hero-photo{left:0;top:75px;width:1200px;height:566px;background:linear-gradient(135deg,#9fb5c9,#c9d3dc 45%,#7f9ab2)}
.hero-curve{left:0;top:560px}
.hero-title{left:0;top:212px;width:1200px;text-align:center;color:var(--white);font-size:40px;font-weight:600;line-height:48px}
.hero-sub{left:0;top:320px;width:1200px;text-align:center;color:var(--white);font-size:13px}
.btn-hero{left:548px;top:397px;width:103px;height:36px;line-height:36px;background:var(--blue-mid)}
/* products */
.product{width:207px;height:193px;background:var(--white);box-shadow:0 2px 10px rgba(0,0,0,.14);display:flex;flex-direction:column;align-items:center;justify-content:center;gap:22px}
.product .icon{width:68px;height:62px;border-radius:10px}
.product .label{display:flex;align-items:center;gap:6px;font-weight:600;color:var(--blue);font-size:19px;letter-spacing:1px}
.product .label i{width:22px;height:22px;border-radius:50%;background:var(--blue);display:block}
/* what is */
.section-title{width:1200px;left:0;text-align:center;font-size:26px;font-weight:600}
.info-card{background:var(--white);overflow:hidden}
.info-card .body{position:absolute;left:20px;top:28px;width:225px;font-size:12.5px;line-height:22px}
.info-card h3{font-size:16px;font-weight:600;color:var(--blue);margin-bottom:6px}
.info-card .more{display:block;margin-top:12px;font-weight:600;color:var(--blue);font-size:13px}
.info-card .photo{position:absolute;top:0;right:0;height:100%}
.tone-light{background:var(--blue-soft)}
.tone-green{background:var(--green)}
.tone-light h3,.tone-light .more,.tone-light .body,.tone-green h3,.tone-green .more,.tone-green .body{color:var(--white)}
/* chart section */
.chart-card{background:var(--white);box-shadow:0 2px 10px rgba(0,0,0,.14)}
.check-list{list-style:none;font-size:13px}
.check-list li{display:flex;align-items:center;gap:10px;height:25.5px}
.check-list li i{width:15px;height:15px;border-radius:50%;border:2px solid var(--blue-soft);display:block}
/* solutions */
.step{width:202px;height:202px;border-radius:50%;background:var(--white);box-shadow:0 4px 0 var(--blue-soft);text-align:center;padding:52px 20px 0}
.step h4{color:var(--blue);font-size:17px;font-weight:600;margin-bottom:6px}
.step p{font-size:13px;line-height:22px}
.step-num{width:52px;height:52px;border-radius:50%;background:var(--blue);color:var(--white);font-weight:600;font-size:18px;line-height:52px;text-align:center}
/* footer */
.footer-col h5{color:var(--white);font-size:14px;font-weight:600;margin-bottom:12px}
.footer-col a{display:block;color:var(--white);font-size:12px;line-height:26px;text-decoration:none}
.contact-row{display:flex;align-items:center;gap:12px;color:var(--white);font-size:12px;height:36px}
.social{width:36px;height:36px;border-radius:50%;display:inline-block;margin-right:12px}
</style>
</head>
<body>

<header class="site-header">
  <div class="brand"><span class="dot"></span>tavo.cr</div>
  <nav class="nav"><span class="active">Inicio</span><span>Soluciones</span><span>Planes</span><span>Contacto</span></nav>
  <a class="abs btn btn-sign">Sign In</a>
  <a class="abs btn btn-trial">Free Trial</a>
</header>

<section>
  <div class="abs hero-photo" role="img" aria-label="Mujer trabajando con documentos contables en una oficina luminosa"></div>
  <svg class="abs hero-curve" width="1200" height="90" viewBox="0 0 1200 90"><path d="M0 82 Q600 -30 1200 82 L1200 90 L0 90Z" fill="#fff"/></svg>
  <h1 class="abs hero-title">Sistema Contable y<br>Facturación en la nube</h1>
  <p class="abs hero-sub">Plataforma 100% en línea para facturar de manera rápida, ágil y sencilla</p>
  <a class="abs btn btn-hero">Free Trial</a>
</section>

<section class="products">
  <div class="abs product" style="left:60px;top:715px"><div class="icon" style="background:#F2A04A" role="img" aria-label="Icono de gráfico de ventas"></div><div class="label"><i></i>VENTAS</div></div>
  <div class="abs product" style="left:293px;top:715px"><div class="icon" style="background:#5FA0D8" role="img" aria-label="Icono de bolsa de compras"></div><div class="label"><i></i>COMPRAS</div></div>
  <div class="abs product" style="left:527px;top:715px"><div class="icon" style="background:#C06BC2" role="img" aria-label="Icono de calculadora"></div><div class="label" style="font-size:15px"><i></i>CONTABILIDAD</div></div>
  <div class="abs product" style="left:760px;top:715px"><div class="icon" style="background:#D9505C" role="img" aria-label="Icono de cajas de inventario"></div><div class="label" style="font-size:16px"><i></i>INVENTARIOS</div></div>
  <div class="abs product" style="left:232px;top:970px"><div class="icon" style="background:#7A7A7A" role="img" aria-label="Icono de edificio bancario"></div><div class="label"><i></i>BANCOS</div></div>
  <div class="abs product" style="left:466px;top:970px"><div class="icon" style="background:#3DB58A" role="img" aria-label="Icono de monedas"></div><div class="label" style="font-size:15px"><i></i>PRESUPUESTO</div></div>
  <div class="abs product" style="left:700px;top:970px"><div class="icon" style="background:#5BB7A8" role="img" aria-label="Icono de equipo de personas"></div><div class="label" style="font-size:17px"><i></i>NÓMINA RH</div></div>
  <div class="abs product" style="left:934px;top:970px"><div class="icon" style="background:#6C7FD0" role="img" aria-label="Icono de apretón de manos"></div><div class="label" style="font-size:24px"><i></i>CRM</div></div>
</section>

<section>
  <svg class="abs" style="left:0;top:1245px" width="1200" height="800" viewBox="0 0 1200 800">
    <path d="M0 6 Q300 60 600 55 Q900 48 1200 0 L1200 760 Q900 740 600 745 Q300 752 0 798Z" fill="var(--blue)"/>
  </svg>
  <h2 class="abs section-title" style="top:1350px;color:var(--white)">¿Qué es TAVO.cr?</h2>

  <article class="abs info-card" style="left:60px;top:1410px;width:524px;height:247px">
    <div class="body"><h3>Prosesional</h3>Lorem Ipsum is simply dummy text of the printing and typesetting industry. Lorem Ipsum has been the industry's standard dummy text ever since the 1500s, when an unknown.<span class="more">más información</span></div>
    <div class="photo" style="width:258px;background:linear-gradient(135deg,#8a7a6a,#c9b8a6)" role="img" aria-label="Profesional sonriendo en su escritorio"></div>
  </article>
  <article class="abs info-card" style="left:615px;top:1410px;width:525px;height:247px">
    <div class="body"><h3>Contador</h3>Lorem Ipsum is simply dummy text of the printing and typesetting industry. Lorem Ipsum has been the industry's standard dummy text ever since the 1500s, when an unknown.<span class="more">más información</span></div>
    <div class="photo" style="width:267px;background:linear-gradient(135deg,#6b4a36,#d8d4cf)" role="img" aria-label="Calculadora y documentos contables sobre una mesa"></div>
  </article>
  <article class="abs info-card tone-light" style="left:60px;top:1686px;width:251px;height:247px">
    <div class="body" style="width:215px"><h3>Micro</h3>Lorem Ipsum is simply dummy text of the printing and typesetting industry. Lorem Ipsum has been the industry's standard dummy text ever since the.<span class="more">más información</span></div>
  </article>
  <article class="abs info-card tone-green" style="left:334px;top:1686px;width:250px;height:247px">
    <div class="body" style="left:18px;width:215px"><h3>PYME</h3>Lorem Ipsum is simply dummy text of the printing and typesetting industry. Lorem Ipsum has been the industry's standard dummy text ever since the.<span class="more">más información</span></div>
  </article>
  <article class="abs info-card" style="left:615px;top:1686px;width:525px;height:247px">
    <div class="body" style="width:215px"><h3>Empresarial</h3>Lorem Ipsum is simply dummy text of the printing and typesetting industry. Lorem Ipsum has been the industry's standard dummy text ever since the.<span class="more">más información</span></div>
    <div class="photo" style="width:258px;background:linear-gradient(135deg,#e6ebef,#3a4656)" role="img" aria-label="Equipo de negocios estrechando manos en una oficina"></div>
  </article>
</section>

<section>
  <h2 class="abs section-title" style="top:2088px;color:var(--blue)">Get Smart Chart of Accounts</h2>
  <h3 class="abs" style="left:60px;top:2202px;font-size:16px;font-weight:600;color:var(--blue)">Lorem Ipsum is simply dummy text.</h3>
  <p class="abs" style="left:60px;top:2234px;width:490px;font-size:13px;line-height:22.5px">Lorem Ipsum is simply dummy text of the printing and typesetting industry. Lorem Ipsum has been the industry's standard dummy text ever since the 1500s, when an unknown printer took a galley of type and scrambled it to make a type specimen book. It has survived not only five centuries, but also the leap into electronic typesetting.</p>
  <ul class="abs check-list" style="left:60px;top:2354px">
    <li><i></i>Lorem Ipsum is simply dummy text of the printing and typesetting.</li>
    <li><i></i>Lorem Ipsum is simply dummy text of the printing and typesetting.</li>
    <li><i></i>Lorem Ipsum is simply dummy text of the printing and typesetting.</li>
  </ul>
  <a class="abs btn" style="left:60px;top:2468px;width:112px;height:37px;line-height:37px;background:var(--blue-mid)">Read More</a>

  <div class="abs chart-card" style="left:673px;top:2175px;width:209px;height:193px">
    <svg width="209" height="193" viewBox="0 0 209 193" font-family="Poppins,sans-serif" font-size="7" fill="#999">
      <g fill="#CADEEF">
        <rect x="21" y="55" width="6" height="45" rx="3"/><rect x="47" y="45" width="6" height="55" rx="3"/><rect x="73" y="60" width="6" height="40" rx="3"/><rect x="99" y="42" width="6" height="58" rx="3"/><rect x="125" y="65" width="6" height="35" rx="3"/><rect x="151" y="48" width="6" height="52" rx="3"/><rect x="177" y="50" width="6" height="50" rx="3"/>
      </g>
      <text x="16" y="112">Mon</text><text x="43" y="112">Tue</text><text x="67" y="112">Wed</text><text x="95" y="112">Thu</text><text x="123" y="112">Fri</text><text x="148" y="112">Sat</text><text x="173" y="112">Sun</text>
      <g fill="#DDE3EC"><rect x="16" y="125" width="70" height="5"/><rect x="16" y="138" width="25" height="4"/><rect x="48" y="138" width="38" height="4"/><rect x="16" y="148" width="70" height="4"/><rect x="16" y="158" width="70" height="4"/><rect x="142" y="125" width="25" height="4"/><rect x="172" y="125" width="25" height="4"/><rect x="142" y="138" width="25" height="4"/><rect x="172" y="138" width="25" height="4"/><rect x="142" y="148" width="25" height="4"/><rect x="172" y="148" width="25" height="4"/></g>
    </svg>
  </div>
  <div class="abs chart-card" style="left:907px;top:2124px;width:208px;height:192px">
    <svg width="208" height="192" viewBox="0 0 208 192">
      <circle cx="103" cy="96" r="62" fill="none" stroke="#DDE0EA" stroke-width="22"/>
      <circle cx="103" cy="96" r="62" fill="none" stroke="#0054AA" stroke-width="22" stroke-dasharray="290 400" transform="rotate(0 103 96)"/>
      <circle cx="103" cy="96" r="62" fill="none" stroke="#7BADD7" stroke-width="22" stroke-dasharray="60 400" transform="rotate(-152 103 96)"/>
    </svg>
  </div>
  <div class="abs chart-card" style="left:673px;top:2401px;width:209px;height:194px;display:flex;align-items:center;justify-content:center">
    <span style="width:150px;height:150px;border-radius:50%;background:var(--blue);display:block"></span>
  </div>
  <div class="abs chart-card" style="left:915px;top:2350px;width:208px;height:191px">
    <svg width="208" height="191" viewBox="0 0 208 191" font-family="Poppins,sans-serif" font-size="7" fill="#999">
      <polyline points="22,100 36,70 58,66 90,45 110,30 140,45" fill="none" stroke="#0054AA" stroke-width="1.5"/>
      <circle cx="36" cy="70" r="3" fill="#fff" stroke="#0054AA"/><circle cx="58" cy="66" r="3" fill="#fff" stroke="#0054AA"/><circle cx="110" cy="30" r="3" fill="#fff" stroke="#0054AA"/>
      <line x1="16" y1="120" x2="190" y2="120" stroke="#DDE3EC"/>
      <text x="16" y="140">Mon</text><text x="43" y="140">Tue</text><text x="67" y="140">Wed</text><text x="95" y="140">Thu</text><text x="123" y="140">Fri</text><text x="148" y="140">Sat</text><text x="173" y="140">Sun</text>
    </svg>
  </div>
</section>

<section>
  <svg class="abs" style="left:0;top:2630px" width="1200" height="480" viewBox="0 0 1200 480">
    <path d="M0 20 Q300 40 600 22 Q900 5 1200 15 L1200 480 L0 480Z" fill="var(--grey-bg)"/>
  </svg>
  <h2 class="abs section-title" style="top:2742px;color:var(--blue)">Nuestras Soluciones</h2>
  <div class="abs step" style="left:60px;top:2823px"><h4>Paga por Uso</h4><p>Paga solo por las funcionalidades que te interesan.</p></div>
  <div class="abs step" style="left:321px;top:2823px"><h4>Sin Contrato</h4><p>Una vez que lo pruebes no te querrás ir. No necesitamos contrato</p></div>
  <div class="abs step" style="left:589px;top:2823px"><h4>En la Nube</h4><p>Desde cualquier lugar y a cualquier hora siempre disponible</p></div>
  <div class="abs step" style="left:850px;top:2823px;padding-top:44px"><h4>Múltiples Dispositivos</h4><p>Accesa a tu información desde tu conmputadora personal, tu tableta o teléfono inteligente</p></div>
  <div class="abs step-num" style="left:187px;top:2804px">1</div>
  <div class="abs step-num" style="left:452px;top:2804px">2</div>
  <div class="abs step-num" style="left:716px;top:2804px">3</div>
  <div class="abs step-num" style="left:966px;top:2802px">4</div>
</section>

<section>
  <svg class="abs" style="left:0;top:3090px" width="1200" height="620" viewBox="0 0 1200 620">
    <rect width="1200" height="620" fill="var(--blue-mist)"/>
    <path d="M0 0 L1200 0 L1200 430 Q900 480 600 445 Q300 410 0 460Z" fill="var(--grey-bg)" opacity="0"/>
    <path d="M0 40 Q250 120 560 60 Q860 0 1200 30 L1200 440 Q900 490 600 455 Q300 420 0 460Z" fill="#6FA3D3"/>
  </svg>
  <svg class="abs" style="left:0;top:3085px" width="1200" height="60" viewBox="0 0 1200 60"><path d="M0 0 L1200 0 L1200 35 Q860 5 560 65 Q250 125 0 45Z" fill="#fff"/></svg>
  <div class="abs" style="left:722px;top:3095px;width:376px;height:376px;border-radius:50%;background:linear-gradient(135deg,#d6dde6,#8aa7c4)" role="img" aria-label="Hombre sonriendo trabajando en su computadora"></div>
  <h2 class="abs" style="left:60px;top:3291px;color:var(--white);font-size:26px;font-weight:500;line-height:37px">¿Qué esperas para crear una cuenta<br>gratis en TAVO.cr?</h2>
  <a class="abs btn" style="left:60px;top:3407px;width:178px;height:36px;line-height:36px;background:var(--white);color:#555">Crear Cuenta Gratis</a>

  <div class="abs brand" style="left:58px;top:3598px"><span class="dot"></span>tavo.cr</div>
  <div class="abs" style="left:426px;top:3612px;width:506px;height:35px;border-radius:18px;background:var(--blue-soft);color:var(--white);font-size:12.5px;line-height:35px;padding-left:20px">Reciba las actualizaciones de Tavo.cr</div>
  <a class="abs btn" style="left:950px;top:3612px;width:123px;height:35px;line-height:35px;background:var(--blue-mid)">Suscribirme</a>
</section>

<footer>
  <svg class="abs" style="left:0;top:3700px" width="1200" height="338" viewBox="0 0 1200 338"><path d="M0 50 Q600 -15 1200 50 L1200 338 L0 338Z" fill="var(--blue)"/><line x1="0" y1="303" x2="1200" y2="303" stroke="#3f7fc4"/></svg>
  <div class="abs footer-col" style="left:60px;top:3768px"><h5>Quick Links</h5><a>Inicio</a><a>Soluciones</a><a>Planes</a><a>Contacto</a></div>
  <div class="abs footer-col" style="left:337px;top:3768px"><h5>Products</h5><a>Ventas</a><a>Compras</a><a>Contabilidad</a><a>Inventarios</a><a>Bancos</a><a>Presupuesto</a><a>Nomina RH</a></div>
  <div class="abs footer-col" style="left:613px;top:3768px"><h5>Contact Us</h5>
    <div class="contact-row"><svg width="16" height="18" viewBox="0 0 16 18"><path d="M8 17 C3 11 2 9 2 7 A6 6 0 0 1 14 7 C14 9 13 11 8 17Z" fill="none" stroke="#fff" stroke-width="1.3"/><circle cx="8" cy="7" r="2" fill="none" stroke="#fff" stroke-width="1.3"/></svg>Calle Ficticia 12, Sabana</div>
    <div class="contact-row"><svg width="16" height="16" viewBox="0 0 16 16"><path d="M3 1 L6 4 L4.5 6 C5.5 8.5 7.5 10.5 10 11.5 L12 10 L15 13 L13 15 C7 14.5 1.5 9 1 3Z" fill="none" stroke="#fff" stroke-width="1.3"/></svg><b style="font-weight:600">4000-1234</b></div>
    <div class="contact-row"><svg width="17" height="12" viewBox="0 0 17 12"><rect x="1" y="1" width="15" height="10" fill="none" stroke="#fff" stroke-width="1.3"/><path d="M1 1 L8.5 7 L16 1" fill="none" stroke="#fff" stroke-width="1.3"/></svg>info@tavo.cr</div>
  </div>
  <div class="abs footer-col" style="left:890px;top:3768px"><h5>Social Links</h5><span class="social" style="background:var(--blue-soft)"></span><span class="social" style="background:var(--white)"></span></div>
  <p class="abs" style="left:0;top:4006px;width:1200px;text-align:center;color:var(--white);font-size:11px">© 2022 Tavo.cr. Todos los derechos reservados.</p>
</footer>

</body>
</html>
```